Bookcover: Lessons From the Silent Orchard

I am publishing a super-low-cost innovation book for €4,99 on Bravolo Self Release to help everyone become a great innovator: young ambitious people without college education nor a big budget. Do you want to help me?

Brief:
Design a book cover 1600 x 2560 pixels for BSR.
Main title: Lessons From the Silent Orchard
Sub title: mindset - insights - skills & tools
Author: Maarten de Klerk
Design: captive, and appealing to everyone
Target Group: young ambitious people without college education

For bravolo please format the height/width ratio of 1.6:1

```html
<!DOCTYPE html>
<html lang="en">
<head>
<meta charset="utf-8">
<title>Lessons From the Silent Orchard – Book Cover</title>
<link rel="stylesheet" href="https://fonts.googleapis.com/css2?family=Montserrat:wght@300;400;700;800&display=swap">
<style>
  :root {
    --page-bg: #e3e3e3;
    --cover-dark: #0d0f10;
    --cover-teal: #12302f;
    --text-light: #ffffff;
    --art-orange: #e8742a;
    --art-red: #c8322a;
    --art-teal: #1f8a7e;
    --art-gold: #e3b04a;
    --art-skin: #c9a88a;
    --art-navy: #1d2a44;
  }
  * { box-sizing: border-box; margin: 0; padding: 0; }
  html, body {
    width: 1200px;
    height: 678px;
    overflow: hidden;
    background: var(--page-bg);
  }
  .canvas {
    position: relative;
    width: 1200px;
    height: 678px;
  }
  .book-cover {
    position: absolute;
    left: 406px;
    top: 29px;
    width: 388px;
    height: 620px;
    overflow: hidden;
    background:
      radial-gradient(ellipse at 80% 40%, var(--cover-teal) 0%, transparent 60%),
      var(--cover-dark);
    font-family: "Montserrat", sans-serif;
    color: var(--text-light);
    text-align: center;
  }
  .cover-art {
    position: absolute;
    left: 0;
    top: 92px;
    width: 388px;
    height: 528px;
    background:
      radial-gradient(ellipse 55% 38% at 70% 62%, var(--art-skin) 0%, rgba(201,168,138,0.5) 40%, transparent 75%),
      radial-gradient(ellipse 30% 25% at 62% 14%, var(--art-red) 0%, transparent 80%),
      radial-gradient(ellipse 45% 35% at 40% 30%, var(--art-teal) 0%, transparent 80%),
      radial-gradient(ellipse 40% 35% at 20% 40%, var(--art-gold) 0%, transparent 80%),
      radial-gradient(ellipse 50% 30% at 50% 95%, var(--art-orange) 0%, var(--art-red) 40%, transparent 85%),
      radial-gradient(ellipse 35% 30% at 55% 70%, var(--art-navy) 0%, transparent 80%);
  }
  .series-line {
    position: absolute;
    top: 22px;
    left: 0;
    width: 100%;
    font-weight: 300;
    font-size: 11px;
    letter-spacing: 0.2px;
  }
  .author-name {
    position: absolute;
    top: 40px;
    left: 0;
    width: 100%;
    font-weight: 800;
    font-size: 20px;
    letter-spacing: 1px;
  }
  .book-title {
    position: absolute;
    left: 0;
    bottom: 40px;
    width: 100%;
    text-transform: uppercase;
    text-shadow: 0 2px 8px rgba(0,0,0,0.35);
    line-height: 1;
  }
  .title-lead {
    display: block;
    font-weight: 700;
    font-size: 12px;
    letter-spacing: 1.5px;
    margin-bottom: 4px;
  }
  .title-main {
    display: block;
    font-weight: 800;
    font-size: 42px;
    letter-spacing: 0.5px;
  }
</style>
</head>
<body>
  <main class="canvas">
    <section class="book-cover">
      <div class="cover-art" role="img" aria-label="Colourful faceted illustration of a human head in profile bursting with geometric shapes in orange, red, teal and gold"></div>
      <p class="series-line">MINDSET - INSIGHTS - SKILLS &amp; TOOLS</p>
      <p class="author-name">MAARTEN DE KLERK</p>
      <h1 class="book-title">
        <span class="title-lead">Lessons from the</span>
        <span class="title-main">Silent</span>
        <span class="title-main">Orchard</span>
      </h1>
    </section>
  </main>
</body>
</html>
```